Wendle Polarworks Inc.
I need double sided standard sized Business Card [3.5" x 2"]
Use fonts similar or same as sample files
Cutting-Edge
Dorian Haswell
Nitrogen Technologist
Bldg 2781 Unit f(6)
58427 Hwy 7C
Ashgrove County Alberta
T9M 5K3
Canada
dorian@wendlepolarworks.com
wendlepolarworks.com
See logo attached. Please use 3D logo
Incorporate the tag line;
Sales - Service - Solutions

```html
<!DOCTYPE html>
<html lang="en">
<head>
<meta charset="utf-8">
<title>Wendle Polarworks Inc. – Business Card Concepts</title>
<link rel="stylesheet" href="https://fonts.googleapis.com/css2?family=PT+Sans:wght@400;700&display=swap">
<style>
  :root {
    --sheet: #ffffff;
    --sheet-edge: #9a9a9a;
    --ink-dark: #0a0a0a;
    --ink-light: #ffffff;
    --brand-blue: #1d8fd8;
    --brand-deep: #0b4f9c;
    --sky-top: #34b6ee;
    --sky-bottom: #0a5fb8;
    --steel-light: #d4d4d4;
    --steel-dark: #6e6e6e;
    --silver: #c9ccd0;
    --text-grey: #3a3a3a;
  }
  * { box-sizing: border-box; margin: 0; padding: 0; }
  html, body {
    width: 1200px; height: 1047px; overflow: hidden;
    background: var(--sheet);
    font-family: "PT Sans", Arial, sans-serif;
  }
  .sheet {
    position: relative; width: 1200px; height: 1047px;
    border: 2px solid var(--sheet-edge);
  }
  .card { position: absolute; overflow: hidden; }

  /* front card */
  .card--front {
    left: 319px; top: 42px; width: 554px; height: 311px;
    background: var(--ink-dark);
    box-shadow: 0 0 0 1px #555;
  }
  .band { position: absolute; left: 0; right: 0; height: 34px;
    background: linear-gradient(90deg, var(--sky-bottom), var(--sky-top)); }
  .band--top { top: 0; }
  .band--bottom { bottom: 0; }
  .rule { position: absolute; left: 0; right: 0; height: 3px; background: var(--silver); }
  .rule--top { top: 42px; }
  .rule--bottom { bottom: 42px; }
  .card--front .brand { position: absolute; left: 28px; top: 120px; }
  .card--front .brand-name { font-size: 19px; }
  .card--front .brand-dot { width: 20px; height: 20px; }
  .contact {
    position: absolute; right: 26px; top: 74px;
    text-align: right; color: var(--ink-light);
  }
  .contact-name { font-size: 21px; font-weight: 400; line-height: 1.1; }
  .contact-role { font-size: 12px; margin-bottom: 44px; }
  .contact-line { font-size: 11px; line-height: 1.5; }

  /* back cards */
  .card--back { width: 550px; height: 311px; }
  .card--white { left: 37px; top: 387px; background: var(--ink-light); border: 1px solid #8a8a8a; }
  .card--blue  { left: 607px; top: 387px; background: linear-gradient(110deg, var(--sky-top), var(--sky-bottom)); }
  .card--black { left: 37px; top: 720px; background: var(--ink-dark); }
  .card--grey  { left: 607px; top: 720px; background: linear-gradient(110deg, var(--steel-light), var(--steel-dark)); }

  .card--back .brand { position: absolute; left: 50px; top: 123px; }
  .card--back .brand-name { font-size: 36px; }
  .card--back .brand-dot { width: 38px; height: 38px; }
  .tagline {
    position: absolute; left: 0; right: 0; top: 236px;
    text-align: center; font-size: 22px; letter-spacing: 0.3px;
  }
  .card--white .tagline { color: var(--text-grey); }
  .card--blue .tagline,
  .card--black .tagline,
  .card--grey .tagline { color: var(--ink-light); }

  .brand { display: flex; align-items: center; gap: 12px; }
  .brand-dot { border-radius: 50%; background: var(--brand-blue); flex: none; }
  .brand-name { font-weight: 700; color: var(--brand-blue); white-space: nowrap; }
  .card--blue .brand-dot { background: var(--brand-deep); }
  .card--blue .brand-name { color: var(--brand-deep); }
</style>
</head>
<body>
<main class="sheet">

  <section class="card card--front" aria-label="Business card front">
    <div class="band band--top"></div>
    <div class="rule rule--top"></div>
    <div class="rule rule--bottom"></div>
    <div class="band band--bottom"></div>
    <div class="brand">
      <span class="brand-dot"></span>
      <span class="brand-name">Wendle Polarworks</span>
    </div>
    <div class="contact">
      <p class="contact-name">Dorian Haswell</p>
      <p class="contact-role">Nitrogen Technologist</p>
      <p class="contact-line">Bldg 2781 Bay 6, 58427 Hwy 7C</p>
      <p class="contact-line">Ashgrove County Alberta, T9M 5K3, Canada</p>
      <p class="contact-line">Phone: 403.555.0148 | Fax: 888.555.0172</p>
      <p class="contact-line">Email: dorian@wendlepolarworks.com</p>
      <p class="contact-line">www.wendlepolarworks.com</p>
    </div>
  </section>

  <section class="card card--back card--white" aria-label="Business card back, white">
    <div class="brand"><span class="brand-dot"></span><span class="brand-name">Wendle Polarworks</span></div>
    <p class="tagline">Sales - Service - Solutions</p>
  </section>

  <section class="card card--back card--blue" aria-label="Business card back, blue">
    <div class="brand"><span class="brand-dot"></span><span class="brand-name">Wendle Polarworks</span></div>
    <p class="tagline">Sales - Service - Solutions</p>
  </section>

  <section class="card card--back card--black" aria-label="Business card back, black">
    <div class="brand"><span class="brand-dot"></span><span class="brand-name">Wendle Polarworks</span></div>
    <p class="tagline">Sales - Service - Solutions</p>
  </section>

  <section class="card card--back card--grey" aria-label="Business card back, grey">
    <div class="brand"><span class="brand-dot"></span><span class="brand-name">Wendle Polarworks</span></div>
    <p class="tagline">Sales - Service - Solutions</p>
  </section>

</main>
</body>
</html>
```